Reid Calloway Fitness Business Card

I Need a really cool and creative yet modern and cutting edge. I run a personal training company, I have a logo already which ill submit images of. Id like the base colors to be black and white with a little red as a highlight color. Charcoal grey is fine also. My clientele is mostly comprised of young professionals who are in touch with modern culture art and are interested in "cool" so if there was one thing i want this business card to be it sexy and cool.

Target Market(s)

young professionals who are image conscious, care about their health, looking and feeling good. They know what is cool and expect the best.

Industry/Entity Type

Training

Requirements
Must have
• - must be a 2 sided card
- must include the following:

Reid Calloway CPT
604 392 7715
Reid@ReidCallowayFitness.example
www.ReidCallowayFitness.example
Nice to have
• id like to see some unconventional shape ideas as well as conventional ones

```html
<!DOCTYPE html>
<html lang="en">
<head>
<meta charset="utf-8">
<title>Reid Calloway Fitness – Business Card</title>
<link rel="stylesheet" href="https://fonts.googleapis.com/css2?family=Questrial&display=swap">
<style>
  :root {
    --paper: #ffffff;
    --backdrop: #f4f4f4;
    --ink: #111111;
    --charcoal: #2b2b2b;
    --accent: #e01b1b;
    --edge: #d9d9d9;
  }
  * { box-sizing: border-box; margin: 0; padding: 0; }
  html, body {
    width: 1200px;
    height: 802px;
    overflow: hidden;
    background: var(--backdrop);
    font-family: "Questrial", "Century Gothic", sans-serif;
    color: var(--ink);
  }
  .canvas { position: relative; width: 1200px; height: 802px; }

  .card {
    position: absolute;
    width: 630px;
    height: 358px;
    background: var(--paper);
    border: 1px solid var(--edge);
    overflow: hidden;
  }
  .card--front { left: 55px; top: 83px; z-index: 2; }
  .card--back  { left: 459px; top: 303px; z-index: 1; }

  .pose-art {
    position: absolute;
    left: 0;
    top: 152px;
    width: 180px;
    height: 202px;
    background: var(--ink);
    border-radius: 0 40px 60px 0 / 0 20px 120px 0;
  }

  .brand {
    position: absolute;
    left: 232px;
    top: 204px;
    width: 178px;
  }
  .brand__name {
    display: flex;
    align-items: center;
    gap: 6px;
    font-size: 14px;
    line-height: 16px;
    white-space: nowrap;
    color: var(--ink);
  }
  .brand__mark {
    flex: none;
    width: 9px;
    height: 9px;
    background: var(--accent);
  }
  .brand__tagline {
    margin-top: 2px;
    text-align: right;
    font-size: 8px;
    line-height: 10px;
    font-style: italic;
    color: var(--charcoal);
  }
  .brand__tagline em { color: var(--accent); }

  .contact {
    position: absolute;
    left: 175px;
    top: 136px;
    width: 260px;
    text-align: center;
    font-style: normal;
    font-size: 15px;
    line-height: 18px;
    white-space: nowrap;
    color: var(--ink);
  }
</style>
</head>
<body>
<main class="canvas">
  <section class="card card--front" aria-label="Card front">
    <div class="pose-art" role="img" aria-label="Large cropped black silhouette of a training pose"></div>
    <div class="brand">
      <p class="brand__name"><span class="brand__mark"></span>Reid Calloway Fitness</p>
      <p class="brand__tagline"><em>Move</em>...Forward</p>
    </div>
  </section>

  <section class="card card--back" aria-label="Card back">
    <address class="contact">
      <p class="contact__name">Reid Calloway CPT</p>
      <p class="contact__phone">604 392 7715</p>
      <p class="contact__email">Reid@ReidCallowayFitness.example</p>
      <p class="contact__web">www.ReidCallowayFitness.example</p>
    </address>
  </section>
</main>
</body>
</html>
```